Electric mountain bike tours nz

We are an Electric Mountain bike tour company in New Zealand. We will be offering bike rental and guided tours around the Nelson region in New Zealand. I want our website to represent both Mountain biking and New Zealand with the colours layout and features. We want tabs for the following:
-1 about us
-2 what we offer
-3 bookings/contact
Under the about us tab will be who we are as a a company. I want the ability to add videos to each of these tabs as we move foward with videos of the tracks we will be riding. I want the website to be editable so I can add and remove videos/photos myself. Also "our bikes" will be under this tab.
Under the what we offer tab will be
-1 bike rental and pricing
-2 guided tours and pricing
-3 recommended package deals.
I want to able to put the tracks under the guided tours tab and select beginner/ intermediate/advanced and have the tracks in each of the following to match the rider level. Also to be able to have a small video of the track would be great in this section.
Bookings and contact tab
(Further information for this tab to be updated soon)
Coded - Design and coding required
1 page
- Silver ferns, kiwi, mountains

```html
<!DOCTYPE html>
<html lang="en">
<head>
<meta charset="utf-8">
<title>TASMANRIDE – Electric Mountain Bike Tours</title>
<link rel="stylesheet" href="https://fonts.googleapis.com/css2?family=Lato:wght@300;400;700;900&display=swap">
<style>
:root{
  --ink:#111;
  --text:#333;
  --muted:#999;
  --topbar:#e6e6e6;
  --band:#e1e1e1;
  --white:#fff;
  --black:#000;
  --green:#48a11c;
  --green-dark:#2f6e10;
  --footer:#1d2328;
  --legal:#d9d9d9;
}
*{box-sizing:border-box;margin:0;padding:0}
html,body{width:1200px;height:4072px;overflow:hidden}
body{font-family:'Lato',sans-serif;color:var(--text);background:var(--white);position:relative}
section,header,footer,div{position:relative}

/* top bar */
.topbar{height:30px;background:var(--topbar);font-size:13px;color:#333;display:flex;align-items:center;justify-content:space-between;padding:0 80px}
.topbar span{display:inline-flex;align-items:center;gap:6px}
.topbar .right{display:flex;gap:30px}
.topbar svg{width:12px;height:12px;fill:#333}

/* header */
.site-header{height:110px;display:flex;align-items:center;justify-content:space-between;padding:0 80px 0 84px}
.brand{display:flex;align-items:center;gap:10px;font-weight:900;font-size:22px;color:var(--ink);letter-spacing:1px}
.brand i{width:34px;height:34px;border-radius:50%;background:var(--ink);display:block}
.nav{display:flex;gap:60px;font-size:14px;font-weight:700;color:var(--ink)}
.nav .active{color:#aaa;font-weight:400}

/* button */
.btn{display:inline-flex;align-items:center;height:40px;background:var(--black);color:var(--white);border-radius:20px;font-size:14px;padding-left:26px;gap:22px;white-space:nowrap;width:max-content}
.btn b{width:40px;height:40px;border-radius:50%;background:var(--white);border:3px solid var(--black);display:flex;align-items:center;justify-content:center;flex:none}
.btn b svg{width:16px;height:16px;fill:none;stroke:var(--black);stroke-width:3}

/* hero */
.hero{height:585px;background:linear-gradient(180deg,#b9a58a 0%,#8f6e4b 35%,#5a3a22 70%,#3a2414 100%);overflow:hidden}
.hero .photo{position:absolute;inset:0;background:radial-gradient(ellipse at 25% 20%,rgba(255,230,190,.55),transparent 55%),radial-gradient(ellipse at 85% 40%,rgba(150,70,30,.5),transparent 60%)}
.hero-copy{position:absolute;left:165px;top:300px;color:var(--white);width:650px}
.hero-copy h1{font-size:58px;font-weight:900;letter-spacing:1px;margin-bottom:14px}
.hero-copy p{font-size:17px;line-height:1.35;margin-bottom:28px}
.arrow{position:absolute;width:30px;height:60px;fill:none;stroke:rgba(255,255,255,.6);stroke-width:4}

/* headings */
.h2{font-size:30px;font-weight:700;color:var(--ink)}
.h2 span{color:var(--muted);font-weight:400}
.center{text-align:center}

/* about */
.about{height:460px;padding:80px 90px 0}
.about .cols{display:flex;justify-content:space-between;margin-top:22px}
.about p{width:610px;font-size:15px;line-height:1.55;color:#444}
.video{width:397px;height:237px;background:linear-gradient(160deg,#c9d6e0,#6e8798 55%,#2c3a44);border:1px solid #222}
.video .play{position:absolute;left:50%;top:45%;transform:translate(-50%,-50%);width:50px;height:50px;border-radius:50%;background:rgba(255,255,255,.85);display:flex;align-items:center;justify-content:center}
.video .bar{position:absolute;left:0;right:0;bottom:0;height:30px;background:#111;display:flex;align-items:center;gap:10px;padding:0 12px}
.video .track{flex:1;height:4px;background:#777;position:relative}
.video .track::before{content:"";position:absolute;left:0;top:0;height:4px;width:30%;background:#d11}
.about .btn{margin-top:30px}

/* our bike */
.our-bike{height:400px;background:var(--band);padding-top:75px;text-align:center}
.our-bike p{width:1000px;margin:24px auto 30px;font-size:14px;line-height:1.6;color:#444}

/* offer */
.offer{height:720px;background:linear-gradient(180deg,#3f4a2a 0%,#6a6230 35%,#8a6a22 60%,#3a2a10 100%);padding-top:55px;text-align:center}
.offer .h2{color:var(--white)}
.offer>p{color:var(--white);font-size:15px;line-height:1.5;width:720px;margin:12px auto 0}
.cards{position:absolute;left:140px;top:222px;display:flex;gap:30px}
.card{width:285px;background:var(--white);border-radius:8px;overflow:hidden;text-align:center}
.card .img{height:242px}
.card h3{font-size:16px;font-weight:700;color:var(--ink);margin:18px 0 10px}
.card p{font-size:12px;line-height:1.45;color:#555;padding:0 26px}
.offer .card{height:405px;overflow:visible}
.offer .card .img{border-radius:8px 8px 0 0}
.offer .card .btn{position:absolute;left:50%;transform:translateX(-50%);bottom:-20px}

/* blog */
.blog{height:640px;background:var(--black);padding-top:55px;text-align:center}
.blog .h2{color:var(--white)}
.blog .cards{top:130px}
.blog .card{height:410px}
.blog .card h3{margin:22px 0 4px}
.blog .date{font-size:12px;color:#555;margin-bottom:16px}
.blog .more{position:absolute;right:22px;bottom:12px;font-size:12px;font-weight:700;color:var(--ink)}

/* testimonials */
.testimonials{height:585px;padding-top:80px;text-align:center}
.quote{position:absolute;top:220px;width:397px;height:240px;border:2px solid #444;border-radius:10px;text-align:left;padding:46px 26px 0 34px;font-size:12px;line-height:1.45;color:#444}
.quote::after{content:"";position:absolute;bottom:-14px;right:40px;width:22px;height:22px;background:var(--white);border-right:2px solid #444;border-bottom:2px solid #444;transform:rotate(45deg)}
.quote .mark{position:absolute;left:16px;top:44px;font-size:26px;font-weight:900;color:var(--ink);line-height:1}
.avatar{position:absolute;top:-50px;left:20px;width:90px;height:90px;border-radius:50%;background:linear-gradient(#b9c3cc,#7d8a96);border:4px solid var(--white);box-shadow:0 0 0 2px #666}
.who{position:absolute;top:495px;font-size:14px;color:var(--ink)}

/* newsletter */
.newsletter{height:75px;background:var(--green);display:flex;align-items:center;padding-left:205px}
.newsletter .icon{width:40px;height:40px;border-radius:50%;background:var(--white);display:flex;align-items:center;justify-content:center;margin-right:14px}
.newsletter h4{color:var(--white);font-size:27px;font-weight:400;margin-right:18px}
.newsletter .field{width:400px;height:34px;background:var(--white);font-size:11px;color:#888;padding:10px 12px;margin-left:20px}
.newsletter .sub{margin-left:14px;height:34px;width:136px;background:var(--green-dark);color:var(--white);font-size:13px;font-weight:700;display:flex;align-items:center;justify-content:center}

/* footer */
.site-footer{height:405px;background:linear-gradient(180deg,#2a3138,#1b2026 60%,#262c2f);color:var(--white)}
.f-brand{position:absolute;left:150px;top:105px;display:flex;align-items:center;gap:10px;font-weight:900;font-size:28px;letter-spacing:1px}
.f-brand i{width:44px;height:44px;border-radius:50%;background:var(--white);display:block}
.f-about{position:absolute;left:160px;top:235px;width:205px;font-size:13px;line-height:1.4;text-align:justify}
.booking{position:absolute;left:453px;top:45px;width:202px;height:325px;background:var(--white);color:var(--ink);padding:18px 22px}
.booking h5{font-size:18px;text-align:center;margin-bottom:10px}
.booking .in{border-bottom:1px solid #aaa;font-size:11px;color:#888;padding:10px 0 4px}
.booking .msg{height:60px}
.booking .send{margin:20px auto 0;width:80px;height:24px;background:var(--black);color:var(--white);font-size:12px;display:flex;align-items:center;justify-content:center}
.contact{position:absolute;left:815px;top:65px;width:220px;font-size:13px;line-height:1.35}
.contact h5{font-size:20px;font-weight:700;padding-bottom:14px;border-bottom:1px solid #666;margin-bottom:16px}
.contact .row{display:flex;gap:8px;align-items:center;margin-top:8px}
.contact .row i{width:12px;height:12px;border-radius:50%;background:var(--white);display:block;flex:none}
.contact h6{font-size:16px;font-weight:700;margin-top:40px;letter-spacing:1px}
.contact .social{display:flex;gap:6px;margin-top:10px}
.contact .social i{width:22px;height:22px;border-radius:50%;background:var(--white);display:block}
.legal{height:62px;background:var(--legal);display:flex;align-items:center;justify-content:center;font-size:14px;color:#444}
</style>
</head>
<body>

<div class="topbar">
  <span><svg viewBox="0 0 12 12"><path d="M6 0a4 4 0 0 0-4 4c0 3 4 8 4 8s4-5 4-8a4 4 0 0 0-4-4z"/></svg>48 Harbour Lane, Nelson, NZ</span>
  <div class="right">
    <span><svg viewBox="0 0 12 12"><path d="M2 0l3 3-1.5 1.5a7 7 0 0 0 4 4L9 7l3 3-2 2C5 12 0 7 0 2z"/></svg>(555) 204 7719</span>
    <span><svg viewBox="0 0 12 12"><path d="M0 2h12v8H0z"/></svg>hello@tasmanride.example</span>
  </div>
</div>

<header class="site-header">
  <div class="brand"><i></i>TASMANRIDE</div>
  <nav class="nav"><span class="active">About us</span><span>What we offer</span><span>Bookings/Contact</span></nav>
</header>

<section class="hero">
  <div class="photo" role="img" aria-label="Rider on an electric mountain bike on a rocky ridge at sunset"></div>
  <svg class="arrow" style="left:55px;top:250px" viewBox="0 0 30 60"><path d="M25 5L5 30l20 25"/></svg>
  <svg class="arrow" style="right:55px;top:250px" viewBox="0 0 30 60"><path d="M5 5l20 25L5 55"/></svg>
  <div class="hero-copy">
    <h1>TASMANRIDE</h1>
    <p>We are an Electric Mountain bike tour company in New Zealand.<br>We will be offering bike rental and guided tours around the Nelson region in New Zealand.</p>
    <span class="btn">Read more<b><svg viewBox="0 0 16 16"><path d="M5 2l6 6-6 6"/></svg></b></span>
  </div>
</section>

<section class="about">
  <h2 class="h2">About <span>Us</span></h2>
  <div class="cols">
    <div>
      <p>Lorem ipsum dolor sit amet, consectetuer adipiscing elit. Aenean commodo ligula eget dolor. Aenean massa. Cum sociis natoque penatibus et magnis dis parturient montes, nascetur ridiculus mus. Donec quam felis, ultricies nec, pellentesque eu, pretium quis, sem. Nulla consequat massa quis enim. Donec pede justo, fringilla vel, aliquet nec, vulputate eget, arcu. In enim justo, rhoncus ut, imperdiet a, venenatis vitae, justo. Nullam dictum felis eu pede mollis pretium. Integer tincidunt. Cras dapibus. Vivamus elementum semper nisi.</p>
      <span class="btn">Read more<b><svg viewBox="0 0 16 16"><path d="M5 2l6 6-6 6"/></svg></b></span>
    </div>
    <div class="video" role="img" aria-label="Video of a rider descending a snowy forest track">
      <div class="play"><svg width="18" height="20" viewBox="0 0 18 20"><path d="M2 1l15 9-15 9z" fill="#222"/></svg></div>
      <div class="bar"><svg width="10" height="12" viewBox="0 0 10 12"><path d="M0 0l10 6-10 6z" fill="#fff"/></svg><div class="track"></div></div>
    </div>
  </div>
</section>

<section class="our-bike">
  <h2 class="h2">Our Bike</h2>
  <p>Lorem ipsum dolor sit amet, consectetuer adipiscing elit. Aenean commodo ligula eget dolor. Aenean massa. Cum sociis natoque penatibus et magnis dis parturient montes, nascetur ridiculus mus. Donec quam felis, ultricies nec, pellentesque eu, pretium quis, sem. Nulla consequat massa quis enim. Donec pede justo, fringilla vel, aliquet nec, vulputate eget, arcu. In enim justo, rhoncus ut, imperdiet a, venenatis vitae, justo. Nullam dictum felis eu pede mollis pretium. Integer tincidunt. Cras dapibus. Vivamus elementum semper nisi.</p>
  <span class="btn">Read more<b><svg viewBox="0 0 16 16"><path d="M5 2l6 6-6 6"/></svg></b></span>
</section>

<section class="offer" role="group" aria-label="What we offer">
  <h2 class="h2">What we Offer</h2>
  <p>Lorem ipsum dolor sit amet, consectetuer adipiscing elit. Aenean commodo ligula eget dolor. Aenean massa. Cum sociis natoque penatibus et magnis dis parturient montes, nascetur ridiculus mus.</p>
  <div class="cards">
    <div class="card">
      <div class="img" role="img" aria-label="Rental bike overlooking a lake and mountains" style="background:linear-gradient(180deg,#9fb7c9,#5d7c93 50%,#3d4f3a)"></div>
      <h3>Bike rental &amp; pricing</h3>
      <p>Lorem ipsum dolor sit amet, consectetuer adipiscing elit. Aenean commodo ligula eget dolor. Aenean massa. Cum sociis natoque penatibus et magnis dis parturient montes, nascetur ridiculus mus.</p>
      <span class="btn">Read more<b><svg viewBox="0 0 16 16"><path d="M5 2l6 6-6 6"/></svg></b></span>
    </div>
    <div class="card">
      <div class="img" role="img" aria-label="Guide and rider with electric bikes" style="background:linear-gradient(180deg,#c9c2b4,#7d7466 55%,#3b3a36)"></div>
      <h3>Guided tours &amp; pricing</h3>
      <p>Lorem ipsum dolor sit amet, consectetuer adipiscing elit. Aenean commodo ligula eget dolor. Aenean massa. Cum sociis natoque penatibus et magnis dis parturient montes, nascetur ridiculus mus.</p>
      <span class="btn">Read more<b><svg viewBox="0 0 16 16"><path d="M5 2l6 6-6 6"/></svg></b></span>
    </div>
    <div class="card">
      <div class="img" role="img" aria-label="Two riders on a green forest trail" style="background:linear-gradient(180deg,#b7cf8a,#6c8f3a 50%,#3c5a22)"></div>
      <h3>Recommended package deals</h3>
      <p>Lorem ipsum dolor sit amet, consectetuer adipiscing elit. Aenean commodo ligula eget dolor. Aenean massa. Cum sociis natoque penatibus et magnis dis parturient montes, nascetur ridiculus mus.</p>
      <span class="btn">Read more<b><svg viewBox="0 0 16 16"><path d="M5 2l6 6-6 6"/></svg></b></span>
    </div>
  </div>
</section>

<section class="blog">
  <h2 class="h2">Latest Blog</h2>
  <svg class="arrow" style="left:55px;top:285px" viewBox="0 0 30 60"><path d="M25 5L5 30l20 25"/></svg>
  <svg class="arrow" style="right:55px;top:285px" viewBox="0 0 30 60"><path d="M5 5l20 25L5 55"/></svg>
  <div class="cards">
    <div class="card">
      <div class="img" role="img" aria-label="Riders below snowy alpine peaks" style="background:linear-gradient(180deg,#a9c3de,#e8eef3 35%,#6d8a4e 75%,#4a6a2c)"></div>
      <h3>Lorem ipsum dolor sit amet</h3><div class="date">October 25, 2017.</div>
      <p>Lorem ipsum dolor sit amet, consectetuer adipiscing elit. Aenean commodo ligula eget dolor. Aenean massa.</p>
      <span class="more">Read more &rsaquo;</span>
    </div>
    <div class="card">
      <div class="img" role="img" aria-label="Rider in a sunlit autumn forest" style="background:linear-gradient(180deg,#d8c58a,#9a8a4a 45%,#5a4a2a)"></div>
      <h3>Lorem ipsum dolor sit amet</h3><div class="date">October 25, 2017.</div>
      <p>Lorem ipsum dolor sit amet, consectetuer adipiscing elit. Aenean commodo ligula eget dolor. Aenean massa.</p>
      <span class="more">Read more &rsaquo;</span>
    </div>
    <div class="card">
      <div class="img" role="img" aria-label="Riders on a grassy hillside trail" style="background:linear-gradient(180deg,#9fb6c4,#5f8a46 45%,#3a5a2a)"></div>
      <h3>Lorem ipsum dolor sit amet</h3><div class="date">October 25, 2017.</div>
      <p>Lorem ipsum dolor sit amet, consectetuer adipiscing elit. Aenean commodo ligula eget dolor. Aenean massa.</p>
      <span class="more">Read more &rsaquo;</span>
    </div>
  </div>
</section>

<section class="testimonials">
  <h2 class="h2">Client <span>Testimonials</span></h2>
  <div class="quote" style="left:150px">
    <div class="avatar" role="img" aria-label="Client portrait"></div>
    <span class="mark">&ldquo;</span>
    Lorem ipsum dolor sit amet, consectetuer adipiscing elit. Quid autem habent admirationis, cum prope accesseris? An hoc usque quaque, aliter in vita? Non igitur de improbo, sed de callido improbo quaerimus, qualis Duo Reges: constructio interrete. Quia nec honesto quic quam honestius nec turpi turpius. Tria genera bonorum; Quid sufficiant sensus? Quae qui non vident, nihil umquam magnum ac cognitione dignum amaverunt. Dicet pro me ipsa virtus nec dubitabit isti vestro beato M. Nihil ad rem! Ne sit sane.
  </div>
  <div class="who" style="left:460px">Carter.A.L.</div>
  <div class="quote" style="left:655px">
    <div class="avatar" role="img" aria-label="Client portrait"></div>
    <span class="mark">&ldquo;</span>
    Lorem ipsum dolor sit amet, consectetuer adipiscing elit. Quid autem habent admirationis, cum prope accesseris? An hoc usque quaque, aliter in vita? Non igitur de improbo, sed de callido improbo quaerimus, qualis Duo Reges: constructio interrete. Quia nec honesto quic quam honestius nec turpi turpius. Tria genera bonorum; Quid sufficiant sensus? Quae qui non vident, nihil umquam magnum ac cognitione dignum amaverunt. Dicet pro me ipsa virtus nec dubitabit isti vestro beato M. Nihil ad rem! Ne sit sane.
  </div>
  <div class="who" style="left:978px">Reid.K.P.</div>
</section>

<section class="newsletter">
  <div class="icon"><svg width="20" height="14" viewBox="0 0 20 14"><rect x="1" y="1" width="18" height="12" fill="none" stroke="#48a11c" stroke-width="2"/><path d="M1 1l9 7 9-7" fill="none" stroke="#48a11c" stroke-width="2"/></svg></div>
  <h4>News letter Signup</h4>
  <svg width="14" height="26" viewBox="0 0 14 26"><path d="M2 2l10 11L2 24" fill="none" stroke="#fff" stroke-width="2"/></svg>
  <div class="field">Enter Your Email</div>
  <div class="sub">SUBSCRIBE</div>
</section>

<footer class="site-footer" role="group" aria-label="Footer over a dark mountain landscape">
  <div class="f-brand"><i></i>TASMANRIDE</div>
  <p class="f-about">Lorem ipsum dolor sit amet, consectetuer adipiscing elit. Aenean commodo ligula eget dolor. Aenean massa. Cum sociis natoque penatibus et magnis dis parturient montes, nascetur ridiculus mus. Donec quam felis, ultricies nec, pellentesque eu.</p>
  <div class="booking">
    <h5>Booking</h5>
    <div class="in">Name</div>
    <div class="in">E-mail</div>
    <div class="in">Phone</div>
    <div class="in msg">Message</div>
    <div class="send">Send</div>
  </div>
  <div class="contact">
    <h5>Contact</h5>
    <div>48 Harbour Lane<br>Nelson, NZ</div>
    <div class="row"><i></i>(555) 204 7719</div>
    <div class="row"><i></i>contact@tasmanride.example</div>
    <div class="row"><i></i>www.tasmanride.example</div>
    <h6>FOLLOW US ON</h6>
    <div class="social"><i></i><i></i><i></i><i></i><i></i></div>
  </div>
</footer>

<div class="legal">© 2017 tasmanride &nbsp;|&nbsp; Privacy Policy &nbsp;|&nbsp; User Agreement</div>

</body>
</html>
```